Artistically challenged consultant needs a sexy business card.

I need a business card design for my consultancy business. I work primarily in the pacific on international development program focusing on tourism, economic empowerment and training. I would like to use a light blue/green to reference the pacific and also a simple design of a sprouting coconut (photo attached for reference) to reference growth and development.
The business card should have icons for email, phone, skype, ABN and linked in.

```html
<!DOCTYPE html>
<html lang="en">
<head>
<meta charset="utf-8">
<title>Mara Ellwood Consulting – Business Card</title>
<link rel="stylesheet" href="https://fonts.googleapis.com/css2?family=Noto+Serif:ital,wght@0,400;1,400&display=swap">
<style>
  :root {
    --page-bg: #e9ebec;
    --card-white: #ffffff;
    --pacific-teal: #22b8a5;
    --lagoon-blue: #8dd6ef;
    --ink-grey: #666666;
    --icon-grey: #6b6b6b;
  }
  html, body {
    margin: 0;
    padding: 0;
    width: 1200px;
    height: 693px;
    overflow: hidden;
    background: var(--page-bg);
  }
  .card {
    position: absolute;
    left: 30px;
    top: 21px;
    width: 1140px;
    height: 650px;
    border-radius: 28px;
    background: var(--pacific-teal);
    overflow: hidden;
    font-family: "Noto Serif", Georgia, serif;
    color: var(--ink-grey);
  }
  .card__face {
    position: absolute;
    left: 15px;
    top: 15px;
    width: 1110px;
    height: 561px;
    background: var(--card-white);
    border-radius: 18px 18px 0 0;
  }
  .card__band {
    position: absolute;
    left: 0;
    bottom: 0;
    width: 1140px;
    height: 74px;
  }
  .sprout-illustration {
    position: absolute;
    left: 73px;
    top: 122px;
    width: 213px;
    height: 350px;
    border-radius: 40% 40% 50% 50% / 30% 30% 40% 40%;
    background: linear-gradient(180deg, rgba(168,194,90,0.35) 0%, rgba(168,194,90,0.2) 45%, rgba(160,105,74,0.35) 75%, rgba(160,105,74,0.45) 100%);
  }
  .brand {
    position: absolute;
    right: 66px;
    top: 92px;
    text-align: right;
    margin: 0;
    font-weight: 400;
  }
  .brand__name {
    display: block;
    font-size: 76px;
    line-height: 94px;
  }
  .brand__tagline {
    display: block;
    font-style: italic;
    font-size: 52px;
    line-height: 56px;
    margin-top: -16px;
  }
  .contacts {
    position: absolute;
    right: 65px;
    top: 350px;
    margin: 0;
    padding: 0;
    list-style: none;
  }
  .contacts__item {
    display: flex;
    justify-content: flex-end;
    align-items: center;
    height: 48px;
    font-size: 35px;
    letter-spacing: 1px;
  }
  .contacts__icon {
    width: 31px;
    height: 31px;
    margin-left: 18px;
    flex: none;
  }
</style>
</head>
<body>
  <div class="card">
    <div class="card__face">
      <div class="sprout-illustration" role="img" aria-label="Line illustration of a sprouting coconut with green leaves"></div>

      <h1 class="brand">
        <span class="brand__name">Mara Ellwood</span>
        <span class="brand__tagline">Consulting</span>
      </h1>

      <ul class="contacts">
        <li class="contacts__item">+61 400 123 456
          <svg class="contacts__icon" viewBox="0 0 30 30" aria-label="Phone">
            <rect width="30" height="30" rx="4" fill="var(--icon-grey)"/>
            <path d="M10 7c1 0 2 3 2 4s-2 1.5-1.5 3 3 4.5 4.5 5 2-1.5 3-1.5 4 1 4 2-1.5 3.5-3.5 3.5C12 23 7 18 7 11c0-2 2-4 3-4z" fill="#fff"/>
          </svg>
        </li>
        <li class="contacts__item">mara ellwood
          <svg class="contacts__icon" viewBox="0 0 30 30" aria-label="Profile">
            <rect width="30" height="30" rx="4" fill="var(--icon-grey)"/>
            <circle cx="15" cy="11" r="4.5" fill="#fff"/>
            <path d="M6.5 24c0-5 3.8-7.5 8.5-7.5s8.5 2.5 8.5 7.5z" fill="#fff"/>
          </svg>
        </li>
        <li class="contacts__item">mara ellwood
          <svg class="contacts__icon" viewBox="0 0 30 30" aria-label="Chat">
            <rect width="30" height="30" rx="4" fill="var(--icon-grey)"/>
            <path d="M7 8h16a1.5 1.5 0 0 1 1.5 1.5v9A1.5 1.5 0 0 1 23 20h-9l-5 4v-4H7a1.5 1.5 0 0 1-1.5-1.5v-9A1.5 1.5 0 0 1 7 8z" fill="#fff"/>
          </svg>
        </li>
        <li class="contacts__item">me@maraellwoodconsulting.com
          <svg class="contacts__icon" viewBox="0 0 30 30" aria-label="Email">
            <rect width="30" height="30" rx="4" fill="var(--icon-grey)"/>
            <rect x="6" y="9" width="18" height="13" fill="#fff"/>
            <path d="M6 9l9 7 9-7" fill="none" stroke="var(--icon-grey)" stroke-width="2"/>
          </svg>
        </li>
      </ul>
    </div>

    <svg class="card__band" viewBox="0 0 1140 74" preserveAspectRatio="none" aria-hidden="true">
      <rect width="1140" height="74" fill="var(--lagoon-blue)"/>
      <polygon points="1009,0 1140,0 1140,74 978,74" fill="var(--pacific-teal)"/>
    </svg>
  </div>
</body>
</html>
```